Web Design Project

The project is about a web design for a brand new dental clinic: Orla Dental Clinic. The dental clinic is located in NSW and the target market is population of all ages (although specialised pediatric dentistry will not be offered at the clinic)
The design is to be:
• Modern
• Professional
• Simple but very attractive
• Logically organised
• Clean
• Fresh
• Engaging
• Friendly
• Creative
Design is to have:
• The dental clinic logo to be shown at the top of every page
• The address and phone number also to be shown at the top of every page
• A link for an online appointment on all pages
• Easy to navigate pages
• Tabs which are easy to identify and read. The tabs are also to be shown at the bottom of each page.
• With drop down menus to be displayed as you scroll along tabs
• Text that is easy to read
• A good use of the colour
• Photos of people smiling. These photos are to be very selective, meaningful and fresh as they play an important role suggesting excellent dental health.
• Short messages
The design is NOT to have:
- Similarities with any other dental clinic (the web design should be authentic and genuine)
- Photos of teeth or smiles on their own or dentists practising the dental work on patients
The site is to include the following pages:
• HOME – this is the welcome page. This page will contain a thank you message and an invitation to visit the dental clinic. It will also have a follow us on chatterloop and quibblr and an area to display testimonials.
• ABOUT US – this page will contain a summary of who we are and the business mission.
• OUR SERVICES – this page is to include a list of the different dental treatments that will be provided at the clinic. Each treatment will have a link to a small window containing a brief description of what the treatment is. This page will also have a section for guarantees on dental work.
• OUR TEAM – this page will have a photo of the professionals that will be working at the clinic and which includes dentists, dental hygienist, dental assistant and administrative assistant.
• OUR TECHNOLOGY – this page will show equipment and technology that we have available at the clinic.
• GALLERY – on this page we will display the ‘before’ and ‘after’ of different treatments conducted, photos of the clinic, etc.
• SPECIAL OFFERS – this page is to contain a list of the discounts available. This page is to include an area to display special offers that will be offered in addition to standard discounts. This page must also include an option for the client to subscribe to our special offers/updates via email. It must also include payment options. It must also include a voucher design which can be printed for discounts.
• LATEST NEWS – this page will include information on latest technical advances on the dental field and may also have links to other documents
• CONTACT US – this page must include:
o the name of the clinic, full address, phone number, fax number, email address
o the business hours
o a location map – link to wayfindly charts
o an option under: Using public transport? Plan your trip at: www.transitplanora.com.au
o an option under: Driving your vehicle? Obtain trip directions at: www.routemellow.com.au
o parking availability
o a ‘print this page’ option
o a photo of the premises for easy identification of the location
• ONLINE APPOINTMENTS – this page must include cells for:
o name
o surname
o mobile number, alternative phone number, email address
o best contact: mobile/alternative number/email
o preferred date and preferred time of the appointment
o are you an existing client/a new patient?
o describe any special needs you may have (e.g. wheelchair access, other)
o how did you hear from us
• TESTIMONIALS/FEEDBACK
I can upload the logo design file upon your request (please specify the type of file required).
In addition to the web design, please indicate if you can undertake the coding for this webpage and if so, please provide a quote.
Updates
Hi there,
Thanks for your interest in this project.
I have uploaded the logo in .jpg, .ai and .eps files. Please feel free to let me know if further information is required.
Best regards,
Moreva

```html
<!DOCTYPE html>
<html lang="en">
<head>
<meta charset="utf-8">
<title>Orla Dental Clinic</title>
<link rel="stylesheet" href="https://fonts.googleapis.com/css2?family=Arimo:ital,wght@0,400;0,700;1,400;1,700&family=Roboto+Condensed:wght@300;400;700&family=Varela+Round&display=swap">
<style>
:root{
  --green:#8dc63f;
  --green-light:#b5dc6a;
  --blue:#0a96d2;
  --blue-light:#5cbde8;
  --text:#222;
  --grey-band:#f1f1f1;
  --grey-line:#d5d5d5;
  --tag-grey:#8a8a8a;
}
*{margin:0;padding:0;box-sizing:border-box}
html,body{width:1200px;height:1031px;overflow:hidden;background:#fff;font-family:Arimo,Arial,sans-serif;color:var(--text)}
.page{position:relative;width:1200px;height:1031px;overflow:hidden}
.top-rule{position:absolute;left:0;top:0;width:1200px;height:6px;background:var(--green)}
.appointment-tab{position:absolute;left:814px;top:0;width:243px;height:40px;background:linear-gradient(#9ccf4a,#b4dc70);
  border-radius:0 0 8px 28px;color:#fff;font:italic 700 17px Arimo,sans-serif;text-align:center;line-height:44px;letter-spacing:.3px}
.brand{position:absolute;left:143px;top:40px;display:flex;align-items:center;gap:10px}
.brand-mark{width:26px;height:26px;border-radius:50%;background:var(--blue)}
.brand-name{font:700 30px "Varela Round",sans-serif;color:var(--blue)}
.tagline{position:absolute;left:328px;top:62px;font:300 22px "Varela Round",sans-serif;color:var(--tag-grey);letter-spacing:.5px}
.contact-top{position:absolute;right:143px;top:54px;text-align:right;color:var(--green)}
.contact-top .phone{font:700 30px "Roboto Condensed",sans-serif;line-height:32px}
.contact-top .address{font:400 17px "Roboto Condensed",sans-serif}
.main-nav{position:absolute;left:143px;top:119px;width:914px;height:38px;background:linear-gradient(#2aa8df,#0b8fcb 55%,#4cb6e4);border-radius:4px;display:flex}
.main-nav a{color:#fff;text-decoration:none;font:700 15px "Roboto Condensed",sans-serif;letter-spacing:.6px;display:flex;align-items:center;justify-content:center;border-right:1px solid rgba(255,255,255,.35)}
.main-nav a:last-child{border-right:0}
.hero{position:absolute;left:143px;top:167px;width:914px;height:285px;background:linear-gradient(100deg,#bfe2f4,#f2d2bc 30%,#e8c0a4 55%,#d9b29a 75%,#cde6f2)}
.welcome{position:absolute;left:143px;top:476px;width:660px}
.welcome h1{font:700 29px Arimo,sans-serif;color:var(--blue);letter-spacing:-.3px}
.welcome .sub{font:300 17px "Roboto Condensed",sans-serif;color:var(--blue);margin-top:-2px}
.welcome p{font:12px/17px Arimo,sans-serif;margin-top:14px;width:650px}
.more{color:var(--green);font:italic 700 12px Arimo,sans-serif;text-decoration:none}
.welcome .more{position:absolute;right:-2px;top:119px}
.premises{position:absolute;left:825px;top:481px;width:232px;height:147px;border:1px solid #bbb;border-radius:4px;padding:5px;background:#fff}
.premises div{width:100%;height:100%;background:linear-gradient(#b9c9d6,#7a5a48 40%,#6b4c3c 80%,#9a9a94)}
.info-band{position:absolute;left:0;top:665px;width:1200px;height:280px;background:var(--grey-band)}
.column{position:absolute;top:24px;width:267px}
.col-location{left:143px}.col-hours{left:467px}.col-testimonials{left:790px}
.divider{position:absolute;top:23px;width:1px;height:237px;background:var(--grey-line)}
.column h2{font:700 25px Arimo,sans-serif;color:var(--blue);line-height:28px}
.column .sub{font:300 15px "Roboto Condensed",sans-serif;color:var(--blue)}
.thumb{width:267px;height:100px;margin-top:13px}
.map{background:linear-gradient(135deg,#efe6c8,#e9d59c 50%,#cfe0b8)}
.headset{background:linear-gradient(90deg,#d7e8c8,#f6efe6 45%,#f0d6c3 70%,#fbf7f2)}
.column .detail{font:700 16px Arimo,sans-serif;color:#333;margin-top:6px;line-height:19px}
.links{text-align:right;margin-top:4px}
.links a{display:block;line-height:16px}
.quote{position:relative;margin-top:14px;height:100px;background:linear-gradient(#bfe3f5,#8ccdec);border:1px solid #5cb4de;border-radius:4px;padding:11px 11px;font:italic 12.5px/16px Arimo,sans-serif;color:#333}
.quote .by{text-align:right;margin-top:1px}
.quote::after{content:"";position:absolute;right:14px;bottom:-13px;border-left:12px solid transparent;border-top:13px solid #8ccdec}
.col-testimonials .links{margin-top:18px}
.footer{position:absolute;left:0;top:945px;width:1200px;height:86px;background:linear-gradient(#0a99d6,#58bce6);color:#fff;text-align:center}
.footer .legal{font:12.5px Arimo,sans-serif;margin-top:31px}
.footer .legal span{margin:0 8px}
.share{display:flex;justify-content:center;gap:14px;margin-top:6px}
.share div{display:flex;font:9px Arimo,sans-serif;height:15px}
.share b{background:#5f7fb8;padding:0 4px;line-height:15px;font-weight:700;border-radius:2px 0 0 2px}
.share i{font-style:normal;background:#fff;color:#333;padding:0 4px;line-height:15px;border-radius:0 2px 2px 0}
</style>
</head>
<body>
<div class="page">
  <div class="top-rule"></div>
  <div class="appointment-tab">ONLINE APPOINTMENT ▸</div>

  <div class="brand"><span class="brand-mark"></span><span class="brand-name">Orla Dental Clinic</span></div>
  <div class="tagline" style="left:380px;top:76px">Values • Innovation • Professionalism</div>

  <div class="contact-top">
    <div class="phone">(02) 5550 0148</div>
    <div class="address">18 Lantern St. Sydney NSW, 2000</div>
  </div>

  <nav class="main-nav">
    <a style="width:133px">ABOUT US ▾</a>
    <a style="width:123px">SERVICES ▾</a>
    <a style="width:149px">SMILE GALLERY</a>
    <a style="width:156px">SPECIAL OFFERS</a>
    <a style="width:83px">NEWS</a>
    <a style="width:139px">TESTIMONIALS</a>
    <a style="width:131px">CONTACT US</a>
  </nav>

  <div class="hero" role="img" aria-label="Photo of a smiling family of four close together"></div>

  <section class="welcome">
    <h1>WELCOME TO ORLA DENTAL CLINIC</h1>
    <div class="sub">We look forward to building a lifelong relationship with you.</div>
    <p>Lorem ipsum dolor sit amet, consectetur adipiscing elit. Vivamus vehicula, elit nec egestas pharetra, orci libero venenatis purus, a lacinia enim odio sed dui. Mauris mi dolor, facilisis ut porttitor sed, volutpat eu odio. Nam risus sem, pulvinar vel ege stas nec, interdum in augue. Sed imperdiet mi tincidunt lectus porttitor bib endum, phasellus vestibulum magna on.</p>
    <a class="more">Read More ▸</a>
  </section>
  <div class="premises"><div role="img" aria-label="Photo of the clinic building on a city street"></div></div>

  <section class="info-band">
    <div class="column col-location">
      <h2>LOCATION</h2>
      <div class="sub">We are located in downtown Sydney.</div>
      <div class="thumb map" role="img" aria-label="Street map of downtown Sydney with the clinic marked"></div>
      <div class="detail">18 Lantern St. Sydney NSW, 2000</div>
      <div class="links"><a class="more">Get Direction ▸</a><a class="more">Use Public Transport ▸</a></div>
    </div>
    <div class="divider" style="left:438px"></div>
    <div class="column col-hours">
      <h2>BUSINESS HOURS</h2>
      <div class="sub">We are open 6 days a week.</div>
      <div class="thumb headset" role="img" aria-label="Photo of a receptionist wearing a headset"></div>
      <div class="detail">Monday – Friday: 9 am to 5 pm<br>Saturday: 9 am to 1 pm</div>
      <div class="links"><a class="more">Make an Online Appointment ▸</a><a class="more">Contact Us ▸</a></div>
    </div>
    <div class="divider" style="left:761px"></div>
    <div class="column col-testimonials">
      <h2>TESTIMONIALS</h2>
      <div class="sub">What people say about us.</div>
      <div class="quote">Lorem ipsum dolor sit amet, consectetur adipi scing elit. Vivamus vehicula, elit nec egestas pharetra, orci libero venenatis puria enim odio sed dui mauris mi.<div class="by">- Dorian Pell</div></div>
      <div class="links"><a class="more">View All Testimonials ▸</a></div>
    </div>
  </section>

  <footer class="footer">
    <div class="legal">Privacy Policy <span>|</span> Disclaimer <span>|</span> ©2012 Orla Dental Clinic. All Rights Reserved.</div>
    <div class="share">
      <div><b>chatterloop</b><i>1212</i></div>
      <div><b>quibblr</b><i>444</i></div>
      <div><b>circlepost</b><i>102</i></div>
    </div>
  </footer>
</div>
</body>
</html>
```